Bref créative
Business Card design for Property Management Company
Harborlight Stewards
Professional
Corwin Talbot
P.O. Box K-4183
Nassau, Bahamas
corwin@harborlightstewardsgroup.com

```html
<!DOCTYPE html>
<html lang="en">
<head>
<meta charset="utf-8">
<title>Harborlight Stewards – Stationery</title>
<link href="https://fonts.googleapis.com/css2?family=Cinzel:wght@400&family=Open+Sans:wght@400&display=swap" rel="stylesheet">
<style>
:root{
  --bg:#eef0f2;
  --paper:#ffffff;
  --blue:#1f5d8c;
  --blue-deep:#123f66;
  --ink:#1a1a1a;
  --text:#555b62;
  --mark:#2a6ea3;
}
*{margin:0;padding:0;box-sizing:border-box}
html,body{width:1200px;height:936px;overflow:hidden;background:var(--bg)}
.canvas{position:relative;width:1200px;height:936px}
.sheet{position:absolute;background:var(--paper);overflow:hidden}
.swoosh{position:absolute;inset:0;width:100%;height:100%}
.brand{position:absolute;display:flex;align-items:center;gap:6px}
.brand-dot{border-radius:50%;background:var(--mark);flex:none}
.brand-name{font-family:"Cinzel",serif;font-weight:400;color:var(--ink);white-space:nowrap}
.contact{position:absolute;font-family:"Open Sans",sans-serif;color:var(--text);line-height:1.5}

.letterhead{left:178px;top:56px;width:393px;height:558px}
.letterhead .brand{left:22px;top:22px}
.letterhead .brand-dot{width:20px;height:20px}
.letterhead .brand-name{font-size:11px}
.watermark{position:absolute;left:137px;top:118px;width:120px;height:120px;border-radius:50%;background:var(--mark);opacity:.08}
.letterhead .contact{left:22px;bottom:20px;font-size:5.5px}

.folder{left:634px;top:38px;width:462px;height:579px}
.folder .brand{left:50%;top:50%;transform:translate(-50%,-50%);gap:12px}
.folder .brand-dot{width:52px;height:52px}
.folder .brand-name{font-size:27px}

.card{left:46px;width:187px;height:90px;border-radius:3px}
.card-front{top:655px}
.card-front .brand{left:10px;top:12px;gap:4px}
.card-front .brand-dot{width:12px;height:12px}
.card-front .brand-name{font-size:7px}
.card-front .contact{left:12px;top:40px;font-size:4.6px}
.card-back{top:761px;background:var(--blue);display:flex;align-items:center;justify-content:center}
.card-back .brand-dot{width:30px;height:30px;background:#f2c14e}

.slip{left:266px;top:672px;width:432px;height:203px}
.slip .brand{left:16px;top:40px;gap:6px}
.slip .brand-dot{width:22px;height:22px}
.slip .brand-name{font-size:13px}
.slip .contact{left:48px;top:68px;font-size:6px}

.envelope{left:741px;top:672px;width:413px;height:203px}
.envelope .web{position:absolute;left:40px;top:22px;font-family:"Cinzel",serif;font-size:9.5px;color:#fff;letter-spacing:.5px}
</style>
</head>
<body>
<main class="canvas">

  <section class="sheet letterhead" aria-label="Letterhead">
    <svg class="swoosh" viewBox="0 0 100 100" preserveAspectRatio="none" aria-hidden="true">
      <path d="M50 0 C70 4 92 12 100 22 L100 0 Z" fill="var(--blue)"/>
      <path d="M44 0 C66 5 90 14 100 25" fill="none" stroke="var(--ink)" stroke-width="1.5" vector-effect="non-scaling-stroke"/>
    </svg>
    <div class="brand"><span class="brand-dot"></span><span class="brand-name">Harborlight Stewards</span></div>
    <div class="watermark" role="img" aria-label="Faint brand circle"></div>
    <div class="contact">Corwin Talbot<br>P.O. Box K-4183<br>Nassau, Bahamas<br>Tel 242 555 0187<br>Fax 242 555 0188<br>corwin@harborlightstewardsgroup.com</div>
  </section>

  <section class="sheet folder" aria-label="Presentation folder">
    <svg class="swoosh" viewBox="0 0 100 100" preserveAspectRatio="none" aria-hidden="true">
      <path d="M0 6 C40 3 85 10 100 27 L100 0 L0 0 Z" fill="var(--blue)"/>
      <path d="M0 8 C40 5 86 12 100 30" fill="none" stroke="var(--ink)" stroke-width="2" vector-effect="non-scaling-stroke"/>
    </svg>
    <div class="brand"><span class="brand-dot"></span><span class="brand-name">Harborlight Stewards</span></div>
  </section>

  <section class="sheet card card-front" aria-label="Business card front">
    <svg class="swoosh" viewBox="0 0 100 100" preserveAspectRatio="none" aria-hidden="true">
      <path d="M52 0 C70 6 88 18 100 34 L100 0 Z" fill="var(--blue)"/>
      <path d="M46 0 C66 7 86 20 100 38" fill="none" stroke="var(--ink)" stroke-width="1" vector-effect="non-scaling-stroke"/>
    </svg>
    <div class="brand"><span class="brand-dot"></span><span class="brand-name">Harborlight Stewards</span></div>
    <div class="contact">Corwin Talbot<br>P.O. Box K-4183, Nassau, Bahamas<br>corwin@harborlightstewardsgroup.com</div>
  </section>

  <section class="sheet card card-back" aria-label="Business card back">
    <span class="brand-dot"></span>
  </section>

  <section class="sheet slip" aria-label="Compliment slip">
    <svg class="swoosh" viewBox="0 0 100 100" preserveAspectRatio="none" aria-hidden="true">
      <path d="M0 0 L100 0 L100 40 C80 18 45 10 0 8 Z" fill="var(--blue)"/>
      <path d="M0 11 C45 13 80 22 100 44" fill="none" stroke="var(--ink)" stroke-width="1.5" vector-effect="non-scaling-stroke"/>
    </svg>
    <div class="brand"><span class="brand-dot"></span><span class="brand-name">Harborlight Stewards</span></div>
    <div class="contact">P.O. Box K-4183, Nassau, Bahamas</div>
  </section>

  <section class="sheet envelope" aria-label="Envelope">
    <svg class="swoosh" viewBox="0 0 100 100" preserveAspectRatio="none" aria-hidden="true">
      <path d="M0 0 L100 0 L100 30 C70 24 30 24 0 28 Z" fill="var(--blue)"/>
    </svg>
    <div class="web">www.harborlightstewardsgroup.com</div>
  </section>

</main>
</body>
</html>
```